Walking Food Tour Business In Melbourne.

We need a two sided A4 page flyer
(1) Front Side - Detailing all the 'foodie' venue stops and other spots of interest. We have one already which is attached. What we are looking for is a better design - rather than just words running down the page. Perhaps something in clouds or boxes/circles relatable to food? However important to note, the venues need to change and therefore the 'user' needs to be able to update the page.
(2) Back Side - The back page, we are looking for a CBD map of Melbourne. I have attached one, but open to a more user friendly one if better suited.
Thank you

```html
<!DOCTYPE html>
<html lang="en">
<head>
<meta charset="utf-8">
<title>Foodies Bucket List Tour – Flyer</title>
<link href="https://fonts.googleapis.com/css2?family=Anton&family=Source+Sans+3:ital,wght@0,400;0,600;0,700;1,600&display=swap" rel="stylesheet">
<style>
  :root{
    --board:#3a3a3c;
    --paper:#ffffff;
    --blue:#0a6fc0;
    --blue-deep:#0d3f86;
    --sky:#39a7e3;
    --sun:#f6cf1a;
    --sun-deep:#e9a90c;
    --brown:#6e3d10;
    --ink:#2b2b2b;
    --muted:#e4e4e4;
  }
  *{box-sizing:border-box;margin:0;padding:0}
  html,body{width:1200px;height:858px;overflow:hidden}
  body{background:var(--board);font-family:"Source Sans 3",sans-serif;color:var(--ink);position:relative}

  .page{position:absolute;top:64px;width:522px;height:730px;background:var(--paper);overflow:hidden}
  .page--front{left:52px}
  .page--back{left:603px}

  /* front header */
  .front-band{position:absolute;left:0;top:0;width:522px;height:330px;background:var(--blue)}
  .front-title{position:absolute;left:0;top:20px;width:100%;text-align:center;font-family:"Anton",sans-serif;font-size:36px;letter-spacing:.5px;color:#fff;text-shadow:2px 2px 0 var(--blue-deep)}
  .hero-photo{position:absolute;left:16px;top:64px;width:494px;height:194px;border:3px solid var(--sun);background:linear-gradient(180deg,#8fb6dd 0%,#c7d9ea 45%,#7b8c9a 70%,#4f6b4a 100%)}
  .hero-shape{position:absolute;left:0;top:180px;width:522px;height:260px}
  .brand-mark{position:absolute;left:204px;top:184px;width:200px;text-align:center;font-weight:700;font-size:22px;color:var(--ink)}

  /* venues */
  .venue{position:absolute;width:230px;font-size:8.2px;line-height:1.25}
  .venue-head{display:flex;align-items:baseline;gap:10px;margin-bottom:3px}
  .venue-name{font-weight:700;font-size:11.5px;color:var(--blue);display:flex;align-items:center;gap:4px;text-transform:uppercase}
  .venue-name::before{content:"";width:10px;height:10px;border-radius:50%;background:var(--sun);border:1px solid var(--sun-deep)}
  .venue-lane{font-weight:600;font-size:8px;color:var(--blue)}

  .contact-pill{position:absolute;left:32px;top:418px;width:222px;height:27px;background:var(--blue-deep);border-radius:14px 14px 0 0;color:#fff;font-size:15px;display:flex;align-items:center;justify-content:center;gap:4px}
  .contact-pill strong{font-weight:700;font-size:17px}

  /* spots */
  .spots{position:absolute;left:0;top:438px;width:522px;height:292px;background:radial-gradient(ellipse at 50% 30%,#fbe14a 0%,var(--sun) 55%,var(--sun-deep) 100%)}
  .spots-title{position:absolute;left:32px;top:20px;font-weight:700;font-size:19.5px;color:var(--brown)}
  .spots-title em{font-style:normal;text-transform:uppercase}
  .spots-divider{position:absolute;left:252px;top:70px;width:1px;height:160px;background:rgba(110,61,16,.35)}
  .spot{position:absolute;width:215px;font-size:8.2px;line-height:1.3;color:var(--brown)}
  .spot-name{font-weight:700;font-size:11.5px;color:#3a2206;display:flex;align-items:center;gap:5px;margin-bottom:4px}
  .spot-name::before{content:"";width:10px;height:10px;border-radius:50%;background:#fff;border:1px solid #b58a30;flex:none}
  .spot-name span{font-weight:400;font-size:8.5px}
  .spots-rule{position:absolute;left:32px;top:250px;width:448px;height:1px;background:rgba(110,61,16,.4)}
  .spots-footer{position:absolute;left:32px;top:255px;color:#fff;font-style:italic;font-weight:600;font-size:12px;text-shadow:1px 1px 1px rgba(0,0,0,.3)}
  .spots-footer strong{font-style:normal;font-weight:700;font-size:17px}

  /* back */
  .city-map{position:absolute;left:71px;top:28px;width:422px;height:674px;background:linear-gradient(135deg,#c9c9c9 0%,#bdbdbd 40%,#b7c98d 62%,#6fa7d8 100%)}
  .back-badge{position:absolute;left:1px;top:228px;width:108px;height:244px;background:#fff;border-radius:0 122px 122px 0}
  .back-brand{position:absolute;left:-40px;top:340px;width:190px;text-align:center;transform:rotate(-90deg);font-weight:700;font-size:20px;color:var(--ink)}
</style>
</head>
<body>

<section class="page page--front">
  <div class="front-band"></div>
  <h1 class="front-title">FOODIES BUCKET LIST TOUR</h1>
  <div class="hero-photo" role="img" aria-label="Photo of the Melbourne riverside with city towers and a footbridge"></div>
  <svg class="hero-shape" viewBox="0 0 522 260" aria-hidden="true">
    <path d="M0 40 C120 70 170 100 250 100 C360 100 440 60 522 50 L522 260 L0 260 Z" fill="#fff"/>
    <path d="M0 36 C60 70 110 72 150 66 C100 86 40 80 0 56 Z" fill="#39a7e3"/>
    <path d="M430 40 C470 60 500 70 522 100 L522 76 C500 54 470 46 430 40 Z" fill="#39a7e3"/>
    <path d="M204 52 A100 100 0 0 1 404 52 L404 52 C380 80 330 94 304 94 C278 94 228 80 204 52 Z" fill="#f6cf1a"/>
    <circle cx="304" cy="52" r="100" fill="#f6cf1a" clip-path="inset(0 0 48% 0)"/>
  </svg>
  <div class="brand-mark" aria-label="Laneway Bites">Laneway Bites</div>

  <div class="venue" style="left:32px;top:295px">
    <div class="venue-head"><span class="venue-name">Tavola Nueva</span><span class="venue-lane">Hosier Lane</span></div>
    <p>Tapas Bar &amp; Restaurant with a graffiti art exterior, Signature Anchoa &amp; Croqueta</p>
  </div>
  <div class="venue" style="left:32px;top:352px">
    <div class="venue-head"><span class="venue-name">Jade Lantern</span><span class="venue-lane" style="margin-left:30px">Oliver Lane</span></div>
    <p>Pan Asian street food flavours. An intriguing Asian influences from Shanghai, Hongkong, Seoul and Japan, Soft Shell Crab or Eggplant Pancake Roll</p>
  </div>
  <div class="venue" style="left:267px;top:276px">
    <div class="venue-head"><span class="venue-name">Ceviche Alto</span><span class="venue-lane" style="margin-left:16px">ACDC Lane</span></div>
    <p>Peruvian bar and grill, Peruano ‘Snapper’ Ceviche, Pastel De Choclo &amp; Alpaca Croquette</p>
  </div>
  <div class="venue" style="left:267px;top:326px">
    <div class="venue-head"><span class="venue-name">Harlow's Chocolate</span><span class="venue-lane">Block Arcade</span></div>
    <p>Founded in 1915 by Alfred Harlow from Adelaide, Signature Frog</p>
  </div>
  <div class="venue" style="left:267px;top:367px">
    <div class="venue-head"><span class="venue-name">Stratus Co</span><span class="venue-lane">Flinders Lane</span></div>
    <p>Described as a ‘local’ eating-house and bar, rather than a restaurant – this favourite with large industrial New York style windows is located in an old rag trade building. Lemon-curd Madeleine &amp; coffee/tea</p>
  </div>

  <div class="contact-pill">Contact: <strong>012.345.6789</strong></div>

  <div class="spots">
    <h2 class="spots-title">Some of our <em>favourite spots</em> on <em>tour</em>…</h2>
    <div class="spots-divider"></div>

    <div class="spot" style="left:32px;top:72px">
      <div class="spot-name">Flinders St Station</div>
      <p>Completed 1909 this station now enjoys 110,000 commuters and 1500 trains daily</p>
    </div>
    <div class="spot" style="left:32px;top:122px">
      <div class="spot-name">Presgrave Place</div>
      <p>With kitschy, framed artworks lining the brick walls, and an old-school laneway vibe. Killer brew at 30ml coffee &amp; cocktails at Ristretto Bar</p>
    </div>
    <div class="spot" style="left:32px;top:184px">
      <div class="spot-name">Block Arcade</div>
      <p>Opened in 1892, visit this Italian designed shopping arcade for the Kettleby Tea Rooms, Spicehaus Herb &amp; Spice Merchants &amp; Harlow's Chocolates</p>
    </div>

    <div class="spot" style="left:268px;top:72px;width:230px">
      <div class="spot-name">Degrave's Street</div>
      <p>Originally a ‘service’ lane, now a vibrant and lively laneway</p>
    </div>
    <div class="spot" style="left:268px;top:111px">
      <div class="spot-name">Royal Arcade</div>
      <p>Opened in 1870, this spectacular Victorian Arcade is the oldest in Australia.</p>
    </div>
    <div class="spot" style="left:268px;top:162px">
      <div class="spot-name">Hosier Lane</div>
      <p>Blue stone laneway with some of our cities best street art embraced</p>
    </div>
    <div class="spot" style="left:268px;top:206px">
      <div class="spot-name">Duckboard Place: <span>Fortuna Bar</span></div>
    </div>
    <div class="spot" style="left:268px;top:225px">
      <div class="spot-name">Malt House Lane: <span>Aqua Vitae Bar - Cocktails</span></div>
    </div>

    <div class="spots-rule"></div>
    <p class="spots-footer">Please contact us for more information: <strong>info@website.com</strong></p>
  </div>
</section>

<section class="page page--back">
  <div class="city-map" role="img" aria-label="Melbourne CBD street map with parks, tram routes, the Yarra River and Docklands, plus a map legend"></div>
  <div class="back-badge"></div>
  <div class="back-brand">Laneway Bites</div>
</section>

</body>
</html>
```